Infectious Diseases Research Laboratory Needs Business Card

We need a business card for an academic research laboratory based in Kansas City called MORVEK. The full lab name is Microbial Dose-Response/Exposure Bridging Studies Laboratory, but this does not need to be incorporated. We study novel ways to optimize the treatment of multidrug-resistant bacterial infections ("superbugs") throughout the entire biomedical research spectrum (from benchtop to bedside). The name MORVEK is not only an acronym for our lab name, but also represents our desire to make discoveries and explore the unknown (the stars, if you well). It also serves as an ode to the state of Kansas motto where we are based, ad astra per aspera ("to the stars, through difficulty").

Target Market(s)

Pharmaceutical companies, researchers

Industry/Entity Type

Pharmaceutical

Contact Information for Business Card

The business card should incorporate and complement our new logo (see uploaded files). Double-sided designs are preferred. Looking for something modern, but professional.

Font styles to use
Sans Serif

Requirements
Must have
• Double-sided. One side would ideally be a solid color incorporating logo and the other should also have the logo (smaller), but incorporate staff information.
• Color codes:
• Red: #F04C51
• Blue: #3477B5
• Gray: #808285

```html
<!DOCTYPE html>
<html lang="en">
<head>
<meta charset="utf-8">
<title>MORVEK business card</title>
<link rel="stylesheet" href="https://fonts.googleapis.com/css2?family=Lato:wght@300;400;700;900&display=swap">
<style>
  :root {
    --red: #F04C51;
    --blue: #3477B5;
    --card-blue: #1F6DB8;
    --gray: #808285;
    --ink: #1b2a3a;
    --paper: #ffffff;
    --backdrop: #e9e6e1;
    --soft: #e3e3e4;
  }
  * { box-sizing: border-box; margin: 0; padding: 0; }
  html, body { width: 1200px; height: 1130px; overflow: hidden; }
  body {
    background: var(--backdrop);
    font-family: "Lato", sans-serif;
    position: relative;
  }
  .card {
    position: absolute;
    left: 145px;
    width: 910px;
    height: 520px;
    overflow: hidden;
    box-shadow: 0 6px 18px rgba(0,0,0,0.15);
  }
  .card-front { top: 30px; background: var(--card-blue); }
  .card-back { top: 580px; background: var(--paper); }

  /* front */
  .front-mark {
    position: absolute;
    left: 170px;
    top: 175px;
    display: flex;
    align-items: center;
    gap: 34px;
  }
  .front-dot {
    width: 120px; height: 120px;
    border-radius: 50%;
    background: var(--ink);
  }
  .front-words { display: flex; flex-direction: column; }
  .front-name {
    font-weight: 400;
    font-size: 118px;
    letter-spacing: 6px;
    line-height: 1;
    color: var(--ink);
  }
  .front-lab {
    margin-top: 8px;
    padding-bottom: 6px;
    border-bottom: 2px solid var(--ink);
    font-size: 12.5px;
    font-weight: 700;
    letter-spacing: 1.4px;
    text-transform: uppercase;
    color: var(--ink);
  }

  /* back */
  .back-decor {
    position: absolute;
    right: 70px;
    top: 40px;
    width: 380px;
    height: 300px;
    border-radius: 50%;
    background: radial-gradient(ellipse at center, var(--soft) 0%, rgba(227,227,228,0.5) 55%, rgba(255,255,255,0) 75%);
  }
  .back-mark {
    position: absolute;
    right: 70px;
    top: 70px;
    display: flex;
    align-items: center;
    gap: 16px;
  }
  .back-dot { width: 46px; height: 46px; border-radius: 50%; background: var(--red); }
  .back-name {
    font-size: 64px;
    font-weight: 400;
    letter-spacing: 3px;
    color: var(--red);
    line-height: 1;
  }
  .person {
    position: absolute;
    left: 60px;
    top: 150px;
    padding-left: 22px;
    border-left: 12px solid var(--red);
  }
  .person-name { font-size: 38px; font-weight: 400; color: var(--ink); line-height: 1.05; }
  .person-name strong { font-weight: 900; }
  .person-role { font-size: 25px; color: var(--red); font-weight: 400; }

  .contacts {
    position: absolute;
    left: 200px;
    top: 300px;
    list-style: none;
  }
  .contacts li {
    display: flex;
    align-items: center;
    gap: 16px;
    height: 40px;
    font-size: 21px;
    font-weight: 300;
    color: var(--ink);
  }
  .contact-icon {
    width: 32px; height: 32px;
    border: 1.5px solid var(--blue);
    border-radius: 50%;
    display: flex; align-items: center; justify-content: center;
  }
  .rule {
    position: absolute;
    left: 0; right: 140px;
    top: 440px;
    height: 3px;
    background: var(--blue);
  }
  .website {
    position: absolute;
    left: 60px;
    top: 455px;
    font-size: 27px;
    color: var(--blue);
  }
  .social {
    position: absolute;
    right: 70px;
    top: 396px;
    display: flex;
    gap: 18px;
  }
  .social span { width: 22px; height: 22px; background: var(--red); border-radius: 3px; }
</style>
</head>
<body>

<section class="card card-front" aria-label="Card front">
  <div class="front-mark">
    <div class="front-dot"></div>
    <div class="front-words">
      <div class="front-name">MORVEK</div>
      <div class="front-lab">Microbial Dose-Response/Exposure Bridging Studies Laboratory</div>
    </div>
  </div>
</section>

<section class="card card-back" aria-label="Card back">
  <div class="back-decor" role="img" aria-label="Soft grey field of scattered circles behind the lab name"></div>
  <div class="back-mark">
    <div class="back-dot"></div>
    <div class="back-name">MORVEK</div>
  </div>

  <div class="person">
    <div class="person-name">Your <strong>Name</strong></div>
    <div class="person-role">Field Service Engineer</div>
  </div>

  <ul class="contacts">
    <li>
      <span class="contact-icon">
        <svg width="18" height="18" viewBox="0 0 24 24"><path fill="#F04C51" d="M6.6 10.8a15 15 0 0 0 6.6 6.6l2.2-2.2c.3-.3.7-.4 1-.2 1.1.4 2.3.6 3.6.6.6 0 1 .4 1 1V20c0 .6-.4 1-1 1A17 17 0 0 1 3 4c0-.6.4-1 1-1h3.5c.6 0 1 .4 1 1 0 1.3.2 2.5.6 3.6.1.3 0 .7-.2 1z"/></svg>
      </span>
      000 000 0000
    </li>
    <li>
      <span class="contact-icon">
        <svg width="16" height="18" viewBox="0 0 16 24"><rect x="2" y="1" width="12" height="22" rx="2" fill="none" stroke="#F04C51" stroke-width="2"/><rect x="5" y="4" width="6" height="9" fill="#F04C51"/><circle cx="8" cy="19" r="1.5" fill="#F04C51"/></svg>
      </span>
      000 000 0000
    </li>
    <li>
      <span class="contact-icon">
        <svg width="18" height="14" viewBox="0 0 24 18"><rect x="1" y="1" width="22" height="16" rx="1" fill="#F04C51"/><path d="M2 2l10 8 10-8" fill="none" stroke="#fff" stroke-width="2"/></svg>
      </span>
      dana.holt@northfieldlabs.net
    </li>
  </ul>

  <div class="social" aria-label="Social profiles"><span></span><span></span><span></span></div>
  <div class="rule"></div>
  <div class="website">www.yourwebsite.com</div>
</section>

</body>
</html>
```